BRISK Form Renewals

12 Week Shape Renewal Scheme

website preview (it's not live yet) :

http://zorvatrainerpage.hostquill.example/preview/7qrwex.5mt3ba28ppdu8.a9416f2c84e329cb57139996de8c679f

colour palette:

RGB codes:

Yellow : R 242,G 206,B 130.
Pink : R 248, G 149,B 133
Dark Pink : R 190,G 108,B 106
Blue : R 38.G 69,B 97#4
Grey : R 78,G 110,B 130

Target Market(s)

Female’s wanting to lose weight, sculpt muscle who are lacking in confidence and feel overwhelmed and don’t know where to start in improving their fitness and lifestyle

Font styles to use
Sans Serif

Colors
fee3d4
ffffff

Requirements
Must have
• My specific colour palette - see above

```html
<!DOCTYPE html>
<html lang="en">
<head>
<meta charset="utf-8">
<title>BRISK Form Renewals – 12 Week Shape Renewal Scheme</title>
<link rel="stylesheet" href="https://fonts.googleapis.com/css2?family=Lato:wght@300;400;700;900&display=swap">
<style>
  :root {
    --pink: #f89585;
    --dark-pink: #be6c6a;
    --blush: #fee3d4;
    --ink: #1f1f1f;
    --paper: #ffffff;
    --photo-light: #f6bcc6;
    --photo-mid: #e58a95;
    --photo-deep: #b44a4c;
  }
  * { margin: 0; padding: 0; box-sizing: border-box; }
  html, body { width: 848px; height: 1200px; overflow: hidden; background: var(--paper); }
  .flyer {
    position: relative; width: 848px; height: 1200px; overflow: hidden;
    background: var(--paper); font-family: "Lato", sans-serif; color: var(--ink);
  }
  .hero-photo {
    position: absolute; left: 0; top: 0; width: 416px; height: 1200px;
    background: linear-gradient(160deg, var(--photo-light) 0%, var(--photo-mid) 55%, var(--photo-deep) 100%);
  }
  .content { position: absolute; right: 82px; text-align: right; }
  .accent { color: var(--pink); }

  .brand { top: 78px; width: 200px; color: var(--pink); font-weight: 900; text-align: center; right: 84px; }
  .brand__name { font-size: 56px; letter-spacing: 10px; line-height: 1; padding-left: 10px; }
  .brand__tag { font-size: 12.5px; letter-spacing: 3.4px; margin-top: 6px; }

  .headline { top: 212px; font-size: 36px; font-weight: 400; letter-spacing: 4.2px; line-height: 35.5px; }
  .headline .accent { font-weight: 700; }

  .rule { position: absolute; right: 82px; width: 67px; height: 2px; background: var(--ink); }
  .rule--pink { background: var(--pink); top: 406px; }
  .rule--one { top: 594px; }
  .rule--two { top: 922px; }

  .icon-badge { position: absolute; right: 82px; width: 44px; height: 44px; }
  .icon-badge--award { top: 459px; }
  .icon-badge--clock { top: 641px; }

  .feature { font-size: 15.5px; line-height: 18.6px; letter-spacing: 0.9px; font-weight: 400; }
  .feature .accent { font-weight: 700; }
  .feature--coach { top: 520px; }
  .feature--result { top: 702px; }

  .intro { top: 774px; width: 290px; font-size: 15.5px; font-weight: 300; line-height: 18.3px; letter-spacing: 0.6px; }
  .intro strong { font-weight: 700; }

  .offer { top: 970px; font-size: 18.5px; letter-spacing: 3.3px; line-height: 23px; }
  .offer__lead { font-weight: 400; }
  .offer__main { font-weight: 700; }
  .offer__free { font-weight: 900; color: var(--pink); }

  .contact { top: 1056px; right: 82px; font-size: 12.6px; line-height: 14px; letter-spacing: 0.3px; }
  .contact__row { display: flex; justify-content: flex-end; align-items: center; gap: 4px; }
  .contact__row svg { width: 11px; height: 11px; }
  .contact__row--plain { padding-right: 15px; }
</style>
</head>
<body>
<main class="flyer">
  <div class="hero-photo" role="img" aria-label="Photo of a woman in a grey sports bra and leggings posing against a pink wall"></div>

  <div class="content brand">
    <div class="brand__name">BRISK</div>
    <div class="brand__tag">FORM RENEWALS</div>
  </div>

  <h1 class="content headline">
    DISCOVER<br>
    THE <span class="accent">12-WEEK</span><br>
    <span class="accent">LIFE-CHANGING</span><br>
    SHAPE RENEWAL<br>
    SCHEME
  </h1>
  <div class="rule rule--pink"></div>

  <svg class="icon-badge icon-badge--award" viewBox="0 0 44 44" aria-hidden="true">
    <circle cx="22" cy="22" r="22" fill="var(--pink)"/>
    <g fill="none" stroke="#fff" stroke-width="1.3" stroke-linejoin="round">
      <circle cx="22" cy="19" r="6.5"/>
      <path d="M18.5 24.5 L17 32 L20 30 L22 32.5 M25.5 24.5 L27 32 L24 30 L22 32.5"/>
    </g>
  </svg>

  <p class="content feature feature--coach">
    IN WEXBRIDGE OR ONLINE, WITH<br>
    WORLD <span class="accent">CHAMPION FIGURE</span><br>
    <span class="accent">ATHLETE MAREN HOLT</span>
  </p>
  <div class="rule rule--one"></div>

  <svg class="icon-badge icon-badge--clock" viewBox="0 0 44 44" aria-hidden="true">
    <circle cx="22" cy="22" r="22" fill="var(--pink)"/>
    <g fill="none" stroke="#fff" stroke-width="1.3" stroke-linecap="round">
      <path d="M29 17 A9 9 0 1 1 24 13.3"/>
      <path d="M18.5 22 L21 24.5 L26 19"/>
    </g>
  </svg>

  <p class="content feature feature--result">
    THE TOTAL TRANSFORMATION<br>
    PROGRAMME <span class="accent">WITH RESULTS</span><br>
    <span class="accent">THAT LAST A LIFETIME</span>
  </p>

  <p class="content intro">
    We’re passionate about helping you lose weight for good and feel happy on the inside and out. <strong>Our programme is tailored to you</strong> and gives the expert advice that’s required to achieve your health and fitness goals, in the easiest, most natural way possible.
  </p>
  <div class="rule rule--two"></div>

  <p class="content offer">
    <span class="offer__lead">GET YOUR FIRST</span><br>
    <span class="offer__main">WORKOUT OR CONSULTATION</span><br>
    <span class="offer__free">FOR FREE!</span>
  </p>

  <address class="content contact" style="font-style: normal;">
    <div class="contact__row">00 987 654 321
      <svg viewBox="0 0 12 12" aria-hidden="true"><path d="M2.5 1 L4.5 1 L5.3 3.6 L4 4.6 C4.7 6.2 5.8 7.3 7.4 8 L8.4 6.7 L11 7.5 L11 9.5 C11 10.3 10.3 11 9.5 11 C5 10.7 1.3 7 1 2.5 C1 1.7 1.7 1 2.5 1 Z" fill="none" stroke="var(--pink)" stroke-width="0.9"/></svg>
    </div>
    <div class="contact__row">ZORVATRAINERPAGE.HOSTQUILL.EXAMPLE
      <svg viewBox="0 0 12 12" aria-hidden="true"><path d="M1.5 6 L6 1.8 L10.5 6 M2.8 5 L2.8 10.5 L9.2 10.5 L9.2 5" fill="none" stroke="var(--pink)" stroke-width="0.9"/></svg>
    </div>
    <div class="contact__row">YOUR ADDRESS &amp; PLACE
      <svg viewBox="0 0 12 12" aria-hidden="true"><path d="M6 11 C3.5 8 2.3 6.2 2.3 4.6 A3.7 3.7 0 0 1 9.7 4.6 C9.7 6.2 8.5 8 6 11 Z" fill="none" stroke="var(--pink)" stroke-width="0.9"/><circle cx="6" cy="4.6" r="1.3" fill="none" stroke="var(--pink)" stroke-width="0.9"/></svg>
    </div>
    <div class="contact__row contact__row--plain">MAREN HOLT BRISK</div>
  </address>
</main>
</body>
</html>
```